Zielgruppe
Wir sind eine Wäscherei.
Zielgruppe: Kunden aus der Hotel- und Gastronomiebranche
Aufgabenstellung
Wir benötigen einen 2-seitigen Flyer DIN lang. 9,8 x21cm
TextInhalte sind in der Vorlage-Datei.
Bilder sind eingefügt.

```html
<!DOCTYPE html>
<html lang="de">
<head>
<meta charset="utf-8">
<title>Serviettenfaltservice – Flyer</title>
<link rel="stylesheet" href="https://fonts.googleapis.com/css2?family=Source+Sans+3:wght@300;400;700&display=swap">
<style>
  :root {
    --magenta: #c4087f;
    --ink: #1d1d1b;
    --paper: #ffffff;
    --photo-light: #eef0f2;
    --photo-mid: #b9bec4;
    --photo-dark: #5d6268;
  }
  html, body {
    margin: 0;
    padding: 0;
    width: 1200px;
    height: 560px;
    overflow: hidden;
    background: var(--paper);
  }
  .flyer {
    position: relative;
    width: 1200px;
    height: 560px;
    background: var(--paper);
    font-family: "Source Sans 3", "Myriad Pro", Arial, sans-serif;
    color: var(--ink);
    overflow: hidden;
  }
  .headline {
    position: absolute;
    left: 44px;
    top: 55px;
    padding-left: 12px;
    border-left: 5px solid var(--magenta);
    color: var(--magenta);
    font-size: 22px;
    line-height: 25px;
  }
  .headline h1 {
    margin: 0;
    font-size: 22px;
    font-weight: 700;
    letter-spacing: 0.2px;
  }
  .headline p {
    margin: 0;
    font-weight: 300;
  }
  .intro {
    position: absolute;
    left: 57px;
    top: 128px;
    margin: 0;
    font-size: 17px;
    line-height: 24.5px;
    font-weight: 400;
  }
  .prices {
    position: absolute;
    left: 57px;
    top: 253px;
    display: flex;
    font-size: 17px;
    line-height: 24.5px;
  }
  .category { width: 314px; }
  .category p { margin: 0; }
  .category .forms { font-weight: 700; }
  .notes {
    position: absolute;
    left: 57px;
    top: 344px;
    margin: 0;
    font-size: 17px;
    line-height: 24.5px;
  }
  .footnote {
    position: absolute;
    left: 57px;
    top: 426px;
    margin: 0;
    font-size: 11px;
  }
  .contact {
    position: absolute;
    left: 57px;
    top: 490px;
    display: flex;
    align-items: center;
    gap: 6px;
    font-size: 12.5px;
    white-space: nowrap;
  }
  .contact .brand {
    color: var(--magenta);
    font-weight: 700;
    font-size: 11px;
    letter-spacing: 0.3px;
    margin-right: 4px;
  }
  .contact .sep {
    color: var(--magenta);
    font-size: 8px;
  }
  .contact svg { display: block; }
  .imagery {
    position: absolute;
    right: 0;
    top: 0;
    width: 330px;
    height: 560px;
  }
</style>
</head>
<body>
<main class="flyer">
  <header class="headline">
    <h1>IHR SERVIETTENFALTSERVICE</h1>
    <p>ab November 2017</p>
  </header>

  <p class="intro">
    Wir optimieren Ihren Serviettenfaltprozess.<br>
    Wir entlasten Sie von dieser demotivierenden und unproduktiven Tätigkeit.<br>
    Wir falten Ihnen Ihre Stoffservietten oder unsere Mietservietten vor.<br>
    Hygienisch, zuverlässig und wirtschaftlich – bereit für die Mise en Place.
  </p>

  <section class="prices">
    <div class="category">
      <p>Faltformen – Kategorie 1:</p>
      <p class="forms">Welle, Kerze, Fächer</p>
      <p>je Faltung für nur 0,20 € *</p>
    </div>
    <div class="category">
      <p>Faltformen – Kategorie 2:</p>
      <p class="forms">Pyramide, Bischofsmütze</p>
      <p>je Faltung für nur 0,35 € *</p>
    </div>
  </section>

  <p class="notes">
    Weitere Formen sind auf Anfrage möglich.<br>
    Bei Bedarf stellen wir Ihnen Mietservietten für nur 0,25 €* je Stück zur Verfügung.<br>
    Mindestabnahmemenge: 100 Stück
  </p>

  <p class="footnote">*zzgl. gesetzliche MwSt.</p>

  <footer class="contact">
    <span class="brand">WÄSCHEREI LINDNER</span>
    <span>Kontakt: Wäscherei Lindner</span>
    <span class="sep">◆</span>
    <span>Birkenweg 14</span>
    <span class="sep">◆</span>
    <span>71634 Talheim</span>
    <svg width="11" height="11" viewBox="0 0 24 24" aria-hidden="true"><path fill="#c4087f" d="M6.6 10.8a15.1 15.1 0 0 0 6.6 6.6l2.2-2.2c.3-.3.7-.4 1-.2 1.1.4 2.3.6 3.6.6.6 0 1 .4 1 1V20c0 .6-.4 1-1 1A17 17 0 0 1 3 4c0-.6.4-1 1-1h3.5c.6 0 1 .4 1 1 0 1.3.2 2.5.6 3.6.1.3 0 .7-.2 1z"/></svg>
    <span>+49 (0) 7100 / 12 34 50</span>
    <svg width="13" height="10" viewBox="0 0 26 20" aria-hidden="true"><rect x="1.5" y="1.5" width="23" height="17" fill="none" stroke="#c4087f" stroke-width="3"/><path d="M2 2l11 9 11-9" fill="none" stroke="#c4087f" stroke-width="3"/></svg>
    <span>info@waescherei-lindner.de</span>
  </footer>

  <svg class="imagery" viewBox="870 0 330 560" preserveAspectRatio="xMidYMid slice">
    <defs>
      <linearGradient id="tableTop" x1="0" y1="0" x2="0.3" y2="1">
        <stop offset="0" stop-color="var(--photo-light)"/>
        <stop offset="0.45" stop-color="var(--photo-mid)"/>
        <stop offset="0.8" stop-color="#d9dcdf"/>
        <stop offset="1" stop-color="#f6f6f6"/>
      </linearGradient>
      <radialGradient id="tableBottom" cx="0.5" cy="0.45" r="0.6">
        <stop offset="0" stop-color="#f4f4f5"/>
        <stop offset="0.55" stop-color="#c9ccd0"/>
        <stop offset="1" stop-color="var(--photo-dark)"/>
      </radialGradient>
    </defs>
    <circle cx="1088" cy="110" r="220" fill="var(--magenta)"/>
    <circle cx="1102" cy="106" r="216" fill="url(#tableTop)" role="img" aria-label="Foto: gedeckter Restauranttisch mit Weingläsern und gefalteten Servietten"/>
    <circle cx="1120" cy="356" r="148" fill="var(--magenta)"/>
    <circle cx="1130" cy="350" r="143" fill="url(#tableBottom)" role="img" aria-label="Foto: Festtafel mit Gläsern und zu Kerzen gefalteten Stoffservietten"/>
  </svg>
</main>
</body>
</html>
```